Eyewear store

-The design must be based around the attached HPID (home page information design) called Lens at Marlowe HPID. I've attached Word and PDF versions - these are the same. The table boxes are just for approximate placement of information – you DON'T have to box everything in and you can arrange these. All fonts used in the HPID are only examples - you can use any Google font you wish.
- Information only is in orange text. Copy to go on the design in black text. Some instructions are in the HPID. Please be creative!
-The design needs to be modern. Colours are to be brown, green, black and white ...refer to the shop images in the HPID. Keep it clean and simple, don't need to use all the colours.
- I've provided the images for the site but these are just to show style, use any similar images, but they must be free images.
Width of content will be 1100 pixels when implemented as a web page. Header height (without nav bar) 150-160 pixels.
If your design is chosen the winning PSD file will have to be provided as follows…
1. Canvas size of 2000px x 2000px - 72ppi in Adobe Photoshop (CS5 compatible)
2. Width of content section is 1100px wide - centered in the canvas
3. Any button rollovers/hovers in the PSD as hidden layers.
4. All fonts used must be Google fonts (except for the fonts in the header at the top of the page).
5. You will need to supply the chosen home page plus one example page (example page as a style guide for how all other pages will look). Example page is only the header and navigational bar at the top, an empty sector in the middle with a column (180 px wide) which can be left or right aligned which means the main sector is 920 pixels wide, and then the footer at the bottom of the page
Checklist - http://pagecraftlist.example/
Target Market(s)
Fashion Eyewear lovers
Mid age women
Sportspeople
Teenagers who need prescription
Non-glasses wearers - People looking to buy branded sunglasses (fashion conscious people of all ages)
Industry/Entity Type
Store
Look and feel
Each slider illustrates characteristics of the customer's brand and the style your logo design should communicate.

```html
<!DOCTYPE html>
<html lang="en">
<head>
<meta charset="utf-8">
<title>Lens at Marlowe – creative eyewear</title>
<link href="https://fonts.googleapis.com/css2?family=Open+Sans:wght@400;600;700&family=Roboto:wght@400;500;700&display=swap" rel="stylesheet">
<style>
:root{
  --green:#5cb814;
  --green-dark:#4a9a0c;
  --ink:#1c1c1c;
  --nav:#222222;
  --footer:#1d1d1d;
  --footer-line:#3a3a3a;
  --grey-band:#e4e4e4;
  --text:#333333;
  --logo:#5a6670;
  --logo-accent:#2f8fc6;
  --white:#ffffff;
}
*{box-sizing:border-box;margin:0;padding:0}
html,body{width:887px;height:1200px;overflow:hidden}
body{position:relative;font-family:"Open Sans",Arial,sans-serif;color:var(--text);background:var(--white)}

/* header */
.site-header{position:absolute;left:0;top:0;width:887px;height:108px;background:linear-gradient(180deg,#f4f4f4 0%,#e6e6e6 100%)}
.brand{position:absolute;left:95px;top:28px}
.brand-name{font-family:"Open Sans",sans-serif;font-weight:700;font-size:27px;letter-spacing:.5px;color:var(--logo);line-height:1}
.brand-tag{font-size:11px;color:var(--logo-accent);text-align:right;margin-top:4px}
.phone-tab{position:absolute;left:639px;top:0;width:170px;height:23px;background:var(--ink);border-radius:0 0 14px 14px;color:var(--white);font-weight:600;font-size:12px;display:flex;align-items:center;justify-content:center;gap:8px}
.address{position:absolute;right:97px;top:38px;font-size:11.5px;font-weight:600;color:var(--ink);display:flex;align-items:center;gap:6px}
.social{position:absolute;right:97px;top:64px;display:flex;gap:4px}
.social span{width:17px;height:17px;border-radius:50%;display:block}

/* nav */
.main-nav{position:absolute;left:0;top:108px;width:887px;height:32px;background:var(--nav);border-bottom:3px solid #111}
.main-nav ul{list-style:none;display:flex;position:absolute;left:95px;top:0;height:29px}
.main-nav li{font-size:10.5px;color:#f0f0f0;padding:0 8px;line-height:29px;border-right:1px solid #3c3c3c}
.main-nav li.active{background:var(--green);color:var(--white);padding:0 14px}

/* hero */
.hero{position:absolute;left:0;top:140px;width:887px;height:319px;
  background:linear-gradient(100deg,#f4dccd 0%,#e9c7b4 14%,#c7a894 24%,#6b7272 34%,#3f4a4e 43%,#8d8471 52%,#c9b38f 62%,#a8936c 72%,#d9c6a3 84%,#f3e8d3 100%)}
.hero-arrow{position:absolute;top:273px;width:38px;height:38px;border-radius:50%;background:rgba(210,200,195,.85)}
.hero-copy{position:absolute;left:515px;top:292px;width:275px}
.hero-title{font-family:Arial,sans-serif;font-size:32px;color:#222;line-height:1.05;letter-spacing:.5px;white-space:nowrap}
.hero-title.green{color:var(--green)}
.hero-text{font-family:Arial,sans-serif;font-weight:700;font-size:11.5px;color:#222;line-height:1.4;margin-top:8px}

/* feature cards */
.features{position:absolute;left:93px;top:479px;display:flex;gap:17px}
.card{width:221px;height:282px;background:var(--white);border-top:3px solid var(--green);box-shadow:0 3px 8px rgba(0,0,0,.15);padding:6px 6px 0}
.card h3{font-family:"Roboto",sans-serif;font-weight:500;font-size:12.5px;color:#222;text-align:center;line-height:1.45;height:40px}
.card-photo{width:209px;height:116px;margin-top:4px;border:1px solid #ddd}
.photo-beach{background:linear-gradient(120deg,#efe4d2 0%,#d9c8ae 30%,#6e5a4e 48%,#e6ddd0 62%,#cdbba0 100%)}
.photo-study{background:linear-gradient(110deg,#f6f4ef 0%,#e9e4da 25%,#b5562f 40%,#f0d44a 55%,#f4f1e9 72%,#c8564c 86%,#6d9fc8 100%)}
.photo-chart{background:linear-gradient(180deg,#f7f7f7 0%,#e6e6e6 35%,#2a2a2a 55%,#cfcfcf 70%,#eeeeee 100%)}
.card p{font-size:9px;line-height:1.42;color:#333;margin-top:10px;padding:0 1px}
.btn{display:inline-block;background:var(--green);color:var(--white);font-family:"Roboto",sans-serif;font-weight:700;font-size:8.5px;padding:7px 10px;border-radius:2px;margin-top:10px;border-bottom:2px solid var(--green-dark)}

/* stores band */
.stores-band{position:absolute;left:0;top:799px;width:887px;height:59px;background:var(--grey-band)}
.stores-band h2{position:absolute;left:231px;top:15px;font-family:"Roboto",sans-serif;font-weight:700;font-size:24px;color:#2b2b2b;letter-spacing:.2px}
.portrait{position:absolute;left:544px;top:783px;width:92px;height:92px;border-radius:50%;border:3px solid #fff;box-shadow:0 0 0 1px #bbb;background:linear-gradient(160deg,#f0f0f0 0%,#bdbdbd 35%,#3a3a3a 60%,#9a9a9a 100%)}

/* clients */
.clients{position:absolute;left:0;top:858px;width:887px;height:119px;background:var(--green)}
.clients h2{position:absolute;left:0;width:887px;top:8px;text-align:center;color:var(--white);font-family:"Roboto",sans-serif;font-weight:700;font-size:19px}
.clients .rule{position:absolute;left:327px;top:37px;width:260px;height:1px;background:rgba(255,255,255,.7)}
.client-row{position:absolute;left:93px;top:49px;width:697px;display:flex;justify-content:space-between}
.client{width:99px;height:51px;background:var(--white);display:flex;align-items:center;justify-content:center;font-family:"Roboto",sans-serif;font-weight:700;font-size:12px;color:#8a8a8a;letter-spacing:.5px}

/* footer */
.site-footer{position:absolute;left:0;top:977px;width:887px;height:190px;background:var(--footer)}
.footer-col{position:absolute;top:14px}
.footer-col h4{font-family:"Roboto",sans-serif;font-weight:500;font-size:13px;color:var(--white);letter-spacing:.3px;padding-bottom:8px;border-bottom:1px solid var(--footer-line)}
.links{left:94px;width:208px}
.links ul{list-style:none;display:grid;grid-template-columns:124px 84px;row-gap:7px;margin-top:10px}
.links li{font-size:9.5px;color:#d8d8d8}
.links li::before{content:"›";color:#aaa;margin-right:6px}
.hours{left:367px;width:150px}
.hours p{font-size:9.5px;color:#d8d8d8;line-height:1.65;white-space:nowrap}
.hours .list{margin-top:6px}
.hours h5{font-family:"Roboto",sans-serif;font-weight:500;font-size:12.5px;color:var(--white);margin-top:8px}
.addr{display:flex;gap:9px;margin-top:6px}
.others{left:590px;width:200px}
.stores-panel{position:absolute;left:584px;top:1022px;width:203px;height:132px;background:#6f6f6f;border-radius:8px;padding:14px 7px}
.store-a{background:#d4d4d4;height:28px;font-family:"Roboto",sans-serif;font-weight:700;font-size:12.5px;color:#333;display:flex;align-items:center;padding-left:6px}
.store-b{display:flex;justify-content:space-between;align-items:center;margin-top:14px;padding:0 6px 4px;border-bottom:1px solid #999;font-family:"Roboto",sans-serif;font-size:13px;color:#eee}
.store-b i{width:16px;height:16px;background:#9a9a9a;display:block}
.visit{display:inline-block;background:var(--white);color:#222;font-size:11px;padding:5px 17px;border-radius:3px;margin:8px 0 0 3px}
.copyright{position:absolute;left:0;top:1167px;width:887px;height:33px;background:#050505;color:var(--white);font-size:9px;text-align:center;line-height:33px}
</style>
</head>
<body>

<header class="site-header">
  <div class="brand">
    <div class="brand-name">LENS AT MARLOWE</div>
    <div class="brand-tag">creative eyewear</div>
  </div>
  <div class="phone-tab">
    <svg width="11" height="11" viewBox="0 0 24 24"><path fill="#fff" d="M6.6 10.8a15.2 15.2 0 006.6 6.6l2.2-2.2a1 1 0 011-.25 11.4 11.4 0 003.6.57 1 1 0 011 1V20a1 1 0 01-1 1A17 17 0 013 4a1 1 0 011-1h3.5a1 1 0 011 1c0 1.25.2 2.45.57 3.57a1 1 0 01-.25 1z"/></svg>
    (06) 555 0148
  </div>
  <div class="address">
    <svg width="10" height="14" viewBox="0 0 10 14"><path fill="#1c1c1c" d="M5 0a5 5 0 00-5 5c0 3.8 5 9 5 9s5-5.2 5-9a5 5 0 00-5-5zm0 7a2 2 0 110-4 2 2 0 010 4z"/></svg>
    12B Harbour Lane, Ashford Bay
  </div>
  <div class="social" aria-label="Social links">
    <span style="background:#3b5b98"></span>
    <span style="background:#2fa9e0"></span>
    <span style="background:#1d77b5"></span>
    <span style="background:#f28a1c"></span>
  </div>
</header>

<nav class="main-nav">
  <ul>
    <li class="active">Home</li>
    <li>About</li>
    <li>Eyewear</li>
    <li>Book An Eye Exam</li>
    <li>Specials/promotions</li>
    <li>All About Eyes</li>
    <li>News</li>
    <li>Articles</li>
    <li>Other Stores</li>
    <li>Contact</li>
  </ul>
</nav>

<section class="hero" role="img" aria-label="Young woman in a dark shirt wearing round sunglasses under a sunlit tree"></section>
<span class="hero-arrow" style="left:49px">
  <svg width="38" height="38" viewBox="0 0 38 38"><path d="M22 11l-8 8 8 8" stroke="#fff" stroke-width="2" fill="none"/></svg>
</span>
<span class="hero-arrow" style="left:797px">
  <svg width="38" height="38" viewBox="0 0 38 38"><path d="M16 11l8 8-8 8" stroke="#fff" stroke-width="2" fill="none"/></svg>
</span>
<div class="hero-copy">
  <div class="hero-title">THREE STORES</div>
  <div class="hero-title green">ONE VISION</div>
  <p class="hero-text">Lorem ipsum dolor sit amet, consectetuer adipiscing elit, sed diam nonummy nibh euismod tincidunt ut laoreet dolore magna aliquam erat</p>
</div>

<section class="features">
  <article class="card">
    <h3>Largest sunglasses selection<br>in Ashford Bay</h3>
    <div class="card-photo photo-beach" role="img" aria-label="Woman in mirrored sunglasses sitting on a sandy beach"></div>
    <p>Lorem ipsum dolor sit amet, consectetuer adipiscing elit, sed diam nonummy nibh euismod tincidunt ut laoreet dolore magna aliquam erat volutpat. Ut wisi enim ad minim veniam, quis nostrud exerci tation ullamcorper</p>
    <span class="btn">READ MORE</span>
  </article>
  <article class="card">
    <h3>Ashford Bay’s Prescription glasses experts – perfect fit guaranteed</h3>
    <div class="card-photo photo-study" role="img" aria-label="Red-haired woman in glasses and a yellow top reading by a colourful bookshelf"></div>
    <p>Lorem ipsum dolor sit amet, consectetuer adipiscing elit, sed diam nonummy nibh euismod tincidunt ut laoreet dolore magna aliquam erat volutpat. Ut wisi enim ad minim veniam, quis nostrud exerci tation ullamcorper</p>
    <span class="btn">READ MORE</span>
  </article>
  <article class="card">
    <h3>For eye exams in the heart of<br>Ashford Bay</h3>
    <div class="card-photo photo-chart" role="img" aria-label="Black framed glasses resting in front of an eye test chart"></div>
    <p>Lorem ipsum dolor sit amet, consectetuer adipiscing elit, sed diam nonummy nibh euismod tincidunt ut laoreet dolore magna aliquam erat volutpat. Ut wisi enim ad minim veniam, quis nostrud exerci tation ullamcorper</p>
    <span class="btn">READ MORE</span>
  </article>
</section>

<section class="stores-band">
  <h2>TWO STORES ONE VISION</h2>
</section>

<section class="clients">
  <h2>Our Clients</h2>
  <span class="rule"></span>
  <div class="client-row">
    <div class="client">NORTHLINE</div>
    <div class="client">VERANO</div>
    <div class="client">CORAL REED</div>
    <div class="client">SOLSTEAD</div>
    <div class="client">BELLATRI</div>
    <div class="client">K.L. MORET</div>
  </div>
</section>
<div class="portrait" role="img" aria-label="Black and white portrait of a woman in glasses"></div>

<footer class="site-footer">
  <div class="footer-col links">
    <h4>QUICK LINKS</h4>
    <ul>
      <li>Home</li><li>All About Eyes</li>
      <li>About</li><li>News</li>
      <li>Eyewear</li><li>Articles</li>
      <li>Book an Eye Exam</li><li>Other Stores</li>
      <li>Specials/Promotions</li><li>Contact</li>
    </ul>
  </div>
  <div class="footer-col hours">
    <h4>OPEN HOURS</h4>
    <div class="list">
      <p>Monday - Friday 9am - 5pm</p>
      <p>Saturday - 9am - 1pm</p>
      <p>Statutory Holidays – closed</p>
    </div>
    <h5>Address</h5>
    <div class="addr">
      <svg width="10" height="14" viewBox="0 0 10 14"><path fill="#fff" d="M5 0a5 5 0 00-5 5c0 3.8 5 9 5 9s5-5.2 5-9a5 5 0 00-5-5zm0 7a2 2 0 110-4 2 2 0 010 4z"/></svg>
      <p>12B Harbour Lane<br>Ashford Bay 4900 New Zealand</p>
    </div>
  </div>
  <div class="footer-col others">
    <h4>OTHER STORES</h4>
  </div>
</footer>
<div class="stores-panel">
  <div class="store-a">Ashford Optic Centre</div>
  <div class="store-b">Kelso Eyecare <i></i></div>
  <span class="visit">View website</span>
</div>

<div class="copyright">Copyright © 2015 Eyewear ,&nbsp; All Rights Reserved</div>

</body>
</html>
```